Help Design the Packaging for our Nicotine Replacement Therapy

Packaging Design Brief for Brevora
We are using this contest to find a designer who can design the packaging for the full line of products listed below for our new brand. This contest will require you to provide designs for the Traditional mint in both the 2mg and 4mg, and the Traditional Cinnamon 2 mg and 4mg, plus the mint in the Modern, 2mg and 4mg. We would like to see how you propose to tie the designs together so their is clear differentiate between the products and flavors, yet it maintains brand cohesiveness.
We would like to then work with the contest winner on a 1-1 project to develop the packaging for the remaining products.
Project Overview:
Brevora is launching a new line of nicotine replacement therapy (NRT) products, including gum and lozenges in multiple flavors and strengths. The packaging design needs to reflect Brevora’s brand values of trust, warmth, professionalism, and customer-centricity while being visually appealing, functional, and easily distinguishable.
Here is our full product line up so you can design product packaging that has the potential to expand as we add more flavors.
Product Line-Up:
1. Nicotine Gum ("Traditional" because it tastes and feels like hollbeck's gum):
- Flavors: Mint, Fruit, Cinnamon
- Strengths: 2mg, 4mg
- Pack Size: 240 pieces per pack
2. Nicotine Gum (Stiffer, Playdough-Like Texture will be called "Classic"):
- Strengths: 2mg, 4mg
3. Nicotine Lozenges:
- Flavors: Mint, Citrus, Berry
- Strengths: 2mg, 4mg
- Pack Size: 120 pieces per pack
Design Objectives:
1. Brand Consistency:
- The Brevora logo should be easily recognizable across all packaging.
- The design should reflect the brand’s personality: trustworthy, professional, warm, and approachable.
- Packaging should evoke a sense of reliability and comfort, appealing to a mature audience.
2. Differentiation:
- Flavor Differentiation:
- Use distinct colors for each flavor to ensure they are easily distinguishable.
- Incorporate icons or images that represent the flavor (e.g., mint leaves for Mint, cinnamon sticks for Cinnamon).
- Strength Differentiation:
- Clearly display the nicotine strength (2mg or 4mg) in a way that stands out at a glance.
- Gum Texture Differentiation:
- Create a visual distinction between the traditional chewing gum and the stiffer, playdough-like gum while maintaining a cohesive brand look.
- Consider using different background textures, patterns, or additional design elements to indicate the different textures while ensuring they still feel part of the same family.
3. Product Type Differentiation:
- Gum vs. Lozenges:
- The lozenges should be visually distinct from the gum products while still fitting within the overall Brevora brand aesthetic.
- Consider using a different shape or design element on the lozenge packaging (e.g., a lozenge icon or a unique pattern) to differentiate them from the gum.
- Maintain consistent use of colors for flavors across both gum and lozenge packaging (e.g., Mint gum and Mint lozenges should share the same color scheme) to unify the product line.
4. Scalability:
- The design should be flexible enough to accommodate additional flavors or product variations in the future.
- Ensure that any new flavor or product type can be easily integrated into the existing design template.
Content Requirements:
1. Front of Pack:
- Brevora logo
- Flavor name and representative image
- Nicotine strength (2mg or 4mg)
- Indication of gum type (Traditional or Stiffer texture)
- Pack size (e.g., "240 Pieces")
2. Here are the die lines from the manufacturer. You will see that there are certain things that must be included on the gum packaging:
https://files.tarnowbox.net/folders/8qpe27Lm_X4v81ZsKd0n-WRyTa3GbU7Hc?usp=share_link
Overall Feel:
- The packaging should communicate that Brevora is a trustworthy, professional brand with a warm, supportive approach. It should feel modern and appeal to a broad audience both male and female.
Packaging design for all SKUs listed above, with clear differentiation between flavors, strengths, and product types.
Here is the link to the brevora logo. https://files.tarnowbox.net/file/d/7-RHbwPqJmm412LcuvzxAq3QWEtn5ZK9S/view?usp=sharing We are not opposed to the color of the dots and + sign changing to signify flavor either.
Target Market(s)
individuals 18-55+ looking to quit vaping and smoking
Industry/Entity Type
nicotine replacement therapy
Other font styles liked:
- should compliment and look good with our logo and font which is Nexa bold
Requirements
Must have
- we want to look professional and trustworthy. . .and we want a design that is cohesive across the product set and can expand and stay on brand with additional flavors.
Nice to have
- We will pick a winner and then pay that winner to do the rest of the package designs for each sku and lozenges too.

```html
<!DOCTYPE html>
<html lang="en">
<head>
<meta charset="utf-8">
<title>Brevora Nicotine Gum – Packaging Line</title>
<link href="https://fonts.googleapis.com/css2?family=Montserrat:wght@400;600;700;800&display=swap" rel="stylesheet">
<style>
  :root {
    --canvas: #f2f2f2;
    --warning-red: #c8101a;
    --ink-light: #ffffff;
    --mint-main: #2fbf78;
    --mint-deep: #0d5a30;
    --mint-soft: #cfeedd;
    --fruit-main: #f08a12;
    --fruit-deep: #e0700a;
    --fruit-soft: #fbe39a;
    --cin-main: #7a1a12;
    --cin-deep: #5a110b;
    --cin-soft: #ead2cf;
  }
  * { box-sizing: border-box; margin: 0; padding: 0; }
  html, body { width: 1200px; height: 793px; overflow: hidden; }
  body {
    background: var(--canvas);
    font-family: "Montserrat", sans-serif;
  }
  .line-grid {
    display: grid;
    grid-template-columns: repeat(3, 400px);
    grid-template-rows: repeat(2, 396px);
  }
  .cell { display: flex; align-items: center; justify-content: center; }

  .flavor-mint { --main: var(--mint-main); --deep: var(--mint-deep); --soft: var(--mint-soft); }
  .flavor-fruit { --main: var(--fruit-main); --deep: var(--fruit-deep); --soft: var(--fruit-soft); }
  .flavor-cinnamon { --main: var(--cin-main); --deep: var(--cin-deep); --soft: var(--cin-soft); }

  .carton { display: flex; height: 340px; box-shadow: 0 6px 18px rgba(0,0,0,.12); }

  /* side panel */
  .side-panel {
    width: 82px; padding: 10px 7px;
    display: flex; flex-direction: column; gap: 8px;
    font-size: 4.6px; line-height: 1.35;
    border-right: 1px solid rgba(0,0,0,.12);
  }
  .drug-facts { border: 0.6px solid currentColor; padding: 3px; }
  .drug-facts .df-title { font-weight: 800; font-size: 5.6px; }
  .warning-box {
    background: var(--warning-red); color: var(--ink-light);
    padding: 7px 5px; font-size: 5.4px; line-height: 1.4; height: 112px;
  }
  .warning-box li { margin-left: 6px; }

  /* front panel */
  .front-panel {
    width: 184px; position: relative; padding-top: 26px;
    display: flex; flex-direction: column; align-items: center;
    text-align: center;
  }
  .type-tag {
    position: absolute; top: 24px; left: 0;
    font-size: 8px; font-weight: 800; letter-spacing: .3px;
    padding: 4px 16px 4px 10px;
    clip-path: polygon(0 0, 100% 0, 88% 100%, 0 100%);
  }
  .brand {
    margin-top: 26px; display: flex; align-items: center; gap: 4px;
    font-size: 24px; font-weight: 700; letter-spacing: -.3px;
  }
  .brand-dot { width: 6px; height: 6px; border-radius: 50%; }
  .product-name { margin-top: 12px; line-height: .9; font-weight: 700; }
  .product-name .nicotine { display: block; font-size: 22px; }
  .product-name .gum { display: block; font-size: 44px; font-weight: 800; }
  .flavor-style { font-size: 8.4px; font-weight: 700; margin-top: 4px; }
  .flavor-name {
    font-size: 9px; letter-spacing: 3px; font-weight: 400; margin-top: 6px;
    padding-top: 5px; border-top: 1.5px solid currentColor; width: 90px;
  }
  .strength-badge {
    position: absolute; left: 14px; bottom: 60px;
    width: 44px; height: 44px; border-radius: 50%;
    display: flex; align-items: center; justify-content: center;
    font-weight: 800; font-size: 12px; border: 2px solid var(--ink-light);
  }
  .flavor-art {
    position: absolute; left: 54px; bottom: 24px; width: 86px; height: 62px;
    border-radius: 10px;
  }
  .count-badge {
    position: absolute; right: 10px; bottom: 30px;
    width: 36px; height: 36px; border-radius: 50%;
    display: flex; flex-direction: column; align-items: center; justify-content: center;
    font-weight: 800; font-size: 10px; line-height: 1;
  }
  .count-badge small { font-size: 3.8px; font-weight: 700; margin-top: 1px; }

  /* traditional: saturated panel, white type */
  .line-traditional .side-panel { background: var(--main); color: rgba(255,255,255,.85); }
  .line-traditional .front-panel {
    background: linear-gradient(160deg, var(--main) 0%, var(--deep) 100%);
    color: var(--ink-light);
  }
  .line-traditional .type-tag { background: var(--ink-light); color: var(--deep); }
  .line-traditional .strength-badge { background: var(--deep); color: var(--ink-light); }
  .line-traditional .count-badge { background: var(--ink-light); color: var(--main); }
  .line-traditional .flavor-art { background: linear-gradient(135deg, var(--soft), #ffffff); }
  .flavor-cinnamon.line-traditional .front-panel { background: linear-gradient(160deg, #6e1711 0%, #4d0e09 100%); }

  /* classic: white panel, flavour-coloured type */
  .line-classic .side-panel { background: #ffffff; color: #555; }
  .line-classic .front-panel {
    background: linear-gradient(180deg, #ffffff 0%, #ffffff 45%, var(--soft) 100%);
    color: var(--main);
  }
  .flavor-mint.line-classic .front-panel { color: #1f8f52; }
  .line-classic .type-tag { background: var(--deep); color: var(--ink-light); }
  .line-classic .strength-badge { background: var(--main); color: var(--ink-light); }
  .line-classic .count-badge { background: var(--ink-light); color: var(--deep); border: 1px solid var(--deep); }
  .flavor-mint.line-classic .count-badge { background: var(--deep); color: var(--ink-light); }
  .line-classic .flavor-art { background: linear-gradient(135deg, var(--soft), #f7f7f7); }
</style>
</head>
<body>
<main class="line-grid">

  <!-- Traditional Mint -->
  <section class="cell">
    <div class="carton flavor-mint line-traditional">
      <aside class="side-panel">
        <div class="drug-facts"><p class="df-title">Drug Facts</p><p>Active ingredient: nicotine polacrilex 2 mg</p><p>Purpose: stop smoking aid</p><p>Questions or comments? Ask a pharmacist</p></div>
        <ul class="warning-box"><li>Not for sale to those under 18 years of age</li><li>Proof of age required</li><li>Not for sale in vending machines or from any source where proof of age cannot be verified</li></ul>
        <p>Pieces sealed in blister units. Do not use if seal is broken.</p><p>Made in USA</p>
      </aside>
      <div class="front-panel">
        <span class="type-tag">TRADITIONAL</span>
        <p class="brand"><span>Brevora</span><span class="brand-dot" style="background:#fff"></span></p>
        <h2 class="product-name"><span class="nicotine">NICOTINE</span><span class="gum">GUM</span></h2>
        <p class="flavor-style">LONG-LASTING FLAVOR</p>
        <p class="flavor-name">MINT</p>
        <div class="flavor-art" role="img" aria-label="Mint leaves with two white gum pellets"></div>
        <span class="strength-badge">2MG</span>
        <span class="count-badge">240<small>PIECES PER PACK</small></span>
      </div>
    </div>
  </section>

  <!-- Traditional Fruit -->
  <section class="cell">
    <div class="carton flavor-fruit line-traditional">
      <aside class="side-panel">
        <div class="drug-facts"><p class="df-title">Drug Facts</p><p>Active ingredient: nicotine polacrilex 2 mg</p><p>Purpose: stop smoking aid</p><p>Questions or comments? Ask a pharmacist</p></div>
        <ul class="warning-box"><li>Not for sale to those under 18 years of age</li><li>Proof of age required</li><li>Not for sale in vending machines or from any source where proof of age cannot be verified</li></ul>
        <p>Pieces sealed in blister units. Do not use if seal is broken.</p><p>Made in USA</p>
      </aside>
      <div class="front-panel">
        <span class="type-tag">TRADITIONAL</span>
        <p class="brand"><span>Brevora</span><span class="brand-dot" style="background:#fff"></span></p>
        <h2 class="product-name"><span class="nicotine">NICOTINE</span><span class="gum">GUM</span></h2>
        <p class="flavor-style">LONG-LASTING FLAVOR</p>
        <p class="flavor-name">FRUIT</p>
        <div class="flavor-art" role="img" aria-label="Pineapple and mixed fruit with two white gum pellets"></div>
        <span class="strength-badge">2MG</span>
        <span class="count-badge">240<small>PIECES PER PACK</small></span>
      </div>
    </div>
  </section>

  <!-- Traditional Cinnamon -->
  <section class="cell">
    <div class="carton flavor-cinnamon line-traditional">
      <aside class="side-panel">
        <div class="drug-facts"><p class="df-title">Drug Facts</p><p>Active ingredient: nicotine polacrilex 2 mg</p><p>Purpose: stop smoking aid</p><p>Questions or comments? Ask a pharmacist</p></div>
        <ul class="warning-box"><li>Not for sale to those under 18 years of age</li><li>Proof of age required</li><li>Not for sale in vending machines or from any source where proof of age cannot be verified</li></ul>
        <p>Pieces sealed in blister units. Do not use if seal is broken.</p><p>Made in USA</p>
      </aside>
      <div class="front-panel">
        <span class="type-tag">TRADITIONAL</span>
        <p class="brand"><span>Brevora</span><span class="brand-dot" style="background:#fff"></span></p>
        <h2 class="product-name"><span class="nicotine">NICOTINE</span><span class="gum">GUM</span></h2>
        <p class="flavor-style">LONG-LASTING FLAVOR</p>
        <p class="flavor-name">CINNAMON</p>
        <div class="flavor-art" role="img" aria-label="Cinnamon sticks and star anise with two white gum pellets"></div>
        <span class="strength-badge">2MG</span>
        <span class="count-badge">240<small>PIECES PER PACK</small></span>
      </div>
    </div>
  </section>

  <!-- Classic Mint -->
  <section class="cell">
    <div class="carton flavor-mint line-classic">
      <aside class="side-panel">
        <div class="drug-facts"><p class="df-title">Drug Facts</p><p>Active ingredient: nicotine polacrilex 2 mg</p><p>Purpose: stop smoking aid</p><p>Questions or comments? Ask a pharmacist</p></div>
        <ul class="warning-box"><li>Not for sale to those under 18 years of age</li><li>Proof of age required</li><li>Not for sale in vending machines or from any source where proof of age cannot be verified</li></ul>
        <p>Pieces sealed in blister units. Do not use if seal is broken.</p><p>Made in USA</p>
      </aside>
      <div class="front-panel">
        <span class="type-tag">CLASSIC</span>
        <p class="brand"><span>Brevora</span><span class="brand-dot" style="background:var(--deep)"></span></p>
        <h2 class="product-name"><span class="nicotine">NICOTINE</span><span class="gum">GUM</span></h2>
        <p class="flavor-style">SHORT BURST FLAVOR</p>
        <p class="flavor-name">MINT</p>
        <div class="flavor-art" role="img" aria-label="Mint leaves with two white gum pellets"></div>
        <span class="strength-badge">2MG</span>
        <span class="count-badge">240<small>PIECES PER PACK</small></span>
      </div>
    </div>
  </section>

  <!-- Classic Fruit -->
  <section class="cell">
    <div class="carton flavor-fruit line-classic">
      <aside class="side-panel">
        <div class="drug-facts"><p class="df-title">Drug Facts</p><p>Active ingredient: nicotine polacrilex 2 mg</p><p>Purpose: stop smoking aid</p><p>Questions or comments? Ask a pharmacist</p></div>
        <ul class="warning-box"><li>Not for sale to those under 18 years of age</li><li>Proof of age required</li><li>Not for sale in vending machines or from any source where proof of age cannot be verified</li></ul>
        <p>Pieces sealed in blister units. Do not use if seal is broken.</p><p>Made in USA</p>
      </aside>
      <div class="front-panel">
        <span class="type-tag">CLASSIC</span>
        <p class="brand"><span>Brevora</span><span class="brand-dot" style="background:var(--main)"></span></p>
        <h2 class="product-name"><span class="nicotine">NICOTINE</span><span class="gum">GUM</span></h2>
        <p class="flavor-style">SHORT BURST FLAVOR</p>
        <p class="flavor-name">FRUIT</p>
        <div class="flavor-art" role="img" aria-label="Pineapple and mixed fruit with two white gum pellets"></div>
        <span class="strength-badge">2MG</span>
        <span class="count-badge">240<small>PIECES PER PACK</small></span>
      </div>
    </div>
  </section>

  <!-- Classic Cinnamon -->
  <section class="cell">
    <div class="carton flavor-cinnamon line-classic">
      <aside class="side-panel">
        <div class="drug-facts"><p class="df-title">Drug Facts</p><p>Active ingredient: nicotine polacrilex 2 mg</p><p>Purpose: stop smoking aid</p><p>Questions or comments? Ask a pharmacist</p></div>
        <ul class="warning-box"><li>Not for sale to those under 18 years of age</li><li>Proof of age required</li><li>Not for sale in vending machines or from any source where proof of age cannot be verified</li></ul>
        <p>Pieces sealed in blister units. Do not use if seal is broken.</p><p>Made in USA</p>
      </aside>
      <div class="front-panel">
        <span class="type-tag">CLASSIC</span>
        <p class="brand"><span>Brevora</span><span class="brand-dot" style="background:var(--main)"></span></p>
        <h2 class="product-name"><span class="nicotine">NICOTINE</span><span class="gum">GUM</span></h2>
        <p class="flavor-style">SHORT BURST FLAVOR</p>
        <p class="flavor-name">CINNAMON</p>
        <div class="flavor-art" role="img" aria-label="Cinnamon sticks and star anise with two white gum pellets"></div>
        <span class="strength-badge">2MG</span>
        <span class="count-badge">240<small>PIECES PER PACK</small></span>
      </div>
    </div>
  </section>

</main>
</body>
</html>
```